A Design Build Company Flyer Ad - Modern, clean [see website for sense of mood, loftmarrow.ca]

We are a Design Build Company . We need to create a full page advertisment that clearly conveys who we are (a design build firm) in a hockey tournament program. A subtle connecting tag line suitable to both our design/build services, and hockey could be wise, example:
- One Team One Dream
- With the right players, anything is possible

Please Note: There have been several submissions that visually attempted to connect hockey with construction, however I think it is a bit confusing- and think it would be best to keep it design/build and our brand consistant.

Please see our website: www.loftmarrow.ca for images, and further inspo on our style.

Target Market(s)

35-50 year olds - higher end real estate market

Industry/Entity Type

Construction: Design, Build

Requirements
Must have
• Our Logo (See attached) Images of work we have completed. (See website: www.loftmarrow.ca)

```html
<!DOCTYPE html>
<html lang="en">
<head>
<meta charset="utf-8">
<title>Harbourline Homes – Tournament Program Ad</title>
<link rel="stylesheet" href="https://fonts.googleapis.com/css2?family=Open+Sans:wght@700;800&family=Lato:wght@300&display=swap">
<style>
  :root {
    --backdrop: #c0c0c0;
    --paper: #ffffff;
    --orange: #ff6600;
    --lime: #dcff3c;
    --green: #6fd65a;
    --ink: #1a1a1a;
    --body: #3a3a3a;
    --photo-light: #dfe7ee;
    --photo-mid: #8fa3bb;
    --photo-dark: #2b3a66;
  }
  * { margin: 0; padding: 0; box-sizing: border-box; }
  html, body {
    width: 901px; height: 1200px; overflow: hidden;
    background: var(--backdrop);
  }
  .flyer {
    position: absolute; left: 110px; top: 114px;
    width: 681px; height: 972px;
    background: var(--paper); overflow: hidden;
  }
  .flyer-art { position: absolute; inset: 0; }
  .hero-title {
    position: absolute; left: 24px; top: 236px;
    color: var(--paper);
    font: 800 59px/60px "Open Sans", sans-serif;
    letter-spacing: -0.5px;
    text-shadow: 2px 3px 4px rgba(0,0,0,.35);
  }
  .brand-seal {
    position: absolute; left: 450px; top: 271px;
    width: 194px; height: 194px; border-radius: 50%;
    background: var(--paper);
    border: 7px solid var(--ink);
    display: flex; align-items: center; justify-content: center;
    text-align: center;
  }
  .brand-name {
    color: var(--ink);
    font: 700 22px/1.15 "Open Sans", sans-serif;
  }
  .headline {
    position: absolute; left: 107px; top: 532px;
    color: var(--orange);
    font: 700 41.5px/44px "Open Sans", sans-serif;
  }
  .features {
    position: absolute; left: 96px; top: 636px;
    display: flex; gap: 36px; list-style: none;
  }
  .feature {
    position: relative; width: 217px; padding-left: 14px;
    color: var(--body);
    font: 300 13.6px/17px "Lato", sans-serif;
  }
  .feature::before {
    content: ""; position: absolute; left: 0; top: 3px;
    width: 10px; height: 10px; background: var(--orange);
  }
  .tagline {
    position: absolute; left: 0; right: 0; top: 800px;
    text-align: center; color: var(--orange);
    font: 300 32px/1 "Lato", sans-serif;
    letter-spacing: -0.5px;
  }
</style>
</head>
<body>
  <main class="flyer">
    <svg class="flyer-art" viewBox="0 0 681 972" width="681" height="972">
      <defs>
        <linearGradient id="photoTone" x1="0" y1="0" x2="1" y2="1">
          <stop offset="0" stop-color="var(--photo-light)"/>
          <stop offset="0.45" stop-color="var(--photo-mid)"/>
          <stop offset="0.75" stop-color="var(--photo-dark)"/>
          <stop offset="1" stop-color="#c4603a"/>
        </linearGradient>
      </defs>
      <polygon class="hero-photo" role="img"
        aria-label="Photo of a youth hockey team seated on the bench holding their sticks"
        points="0,0 681,0 681,260 0,485" fill="url(#photoTone)"/>

      <g class="accent-stripes" style="mix-blend-mode:multiply">
        <polygon points="0,498 310,395 300,412 0,518" fill="var(--green)" opacity=".8"/>
        <polygon points="0,513 681,288 681,310 0,545" fill="var(--lime)"/>
        <polygon points="268,403 681,262 681,298 248,444" fill="var(--orange)" opacity=".95"/>
      </g>

      <g class="accent-stripes" style="mix-blend-mode:multiply">
        <polygon points="290,972 560,883 545,903 330,972" fill="var(--green)" opacity=".8"/>
        <polygon points="455,972 681,893 681,925 545,972" fill="var(--lime)"/>
        <polygon points="505,880 681,826 681,868 473,937" fill="var(--orange)" opacity=".95"/>
      </g>
    </svg>

    <h1 class="hero-title">ONE TEAM<br>ONE DREAM</h1>

    <div class="brand-seal">
      <span class="brand-name">HARBOURLINE<br>HOMES</span>
    </div>

    <h2 class="headline">With the right players,<br>anything is possible</h2>

    <ul class="features">
      <li class="feature">Lorem Ipsum is simply dummy text of the printing and typesetting industry. Lorem Ipsum has been the industry's standard dummy text ever since the 1500s, when an unknown printer took a galley of type and scrambled it to make a type specimen book.</li>
      <li class="feature">Lorem Ipsum is simply dummy text of the printing and typesetting industry. Lorem Ipsum has been the industry's standard dummy text ever since the 1500s, when an unknown printer took a galley of type and scrambled it to make a type specimen book.</li>
    </ul>

    <p class="tagline">THIS IS MY HAPPY PLACE</p>
  </main>
</body>
</html>
```